Swimming Pool Service business card needed!!!! Please

Hi Everyone! Thanks for looking at my contest. I PROMISE to provide excellent feedback during this process.

I am starting a new swimming pool cleaning business in San Diego, California and would like your help in making a business card for me.

I like easy to read, classy and sophisticated.

I am having a website designed and I'm looking for it to have pictures of really clean & clear pools.

I really like the blue on white color format, but open to other colors.

I do not have a logo, but the name of my company is GLIMMERTIDE POOL SERVICE.

My tag line is: Pools so clean, you can see yourself "in" them. (does not need to have the quotes around "in"...maybe just italics for this word IN?) You decide for me.

I would like to have a logo designed that incorporates some sort of easy to read letters. I do not want cursive (handwriting) letters. I thought about having a "reflection" of letters (mirror image), but think that this will be hard to read from far away. Maybe you can surprise me and come up with an idea that works using the a mirror image....but I'm not sure. I was leaning toward plain old BLOCK letters as I think it would be easy to read on my truck.

I would like to have the NAQTR and WBK logos on the back of the card. I have attached those two as files. You can put other things on the back as well, but I need these two logos on there. Or maybe put them on the front of the card if you have a better idea for the back of the card! :-)

Maybe blue on the back of the card and white on the front of the card? I don't know, I'm just thinking out loud.

I had another card done awhile ago called HARBORLINE TEES. I have uploaded a copy of that card for your reference. I don't want this card to be the same as my new company is a swimming pool cleaning company, but I wanted you to see what I liked in the past.

THANK YOU!!!!
Updates

Reason: Partner out of town and want their feedback....so need more time to decide and designs still coming in.

Industry/Entity Type

Business

Contact Information for Business Card

GLIMMERTIDE POOL SERVICE
Dale Wexby
Owner
4817 Quarry Bend Ave. #512
San Diego, CA 92417
858-291-6083
www.glimmertidepoolservice.example

Font styles to use
Sans Serif

Colors
0255a3
3176b5
ffffff

Requirements
Nice to have
• Some things to (possibly) add to back of card (in no particular order)
• WBK logo
• NAQTR logo
• Free Estimates
• Residential and Commercial Services
• Equipment Repairs
• Saltwater Systems
• Licensed, Bonded, Insured
• Family Owned and Operated
• No Contracts
• =======================
• Check out the FolioMint business card that i attached.
• i think they did this using a chrome overlay.
• Can any of you guys design that? or is that done at my printer?
• ==================
Should not have
• Hi Designers-
• The first round of cards came back and let's stay away from the light blue (powder blue) color. I don't like the look of it on the business cards.
• Also, the pool company JPG's that I attached are other logos of pool companies that I liked. I don't want them to be on my card. The only logos that should be on my card are the one you are going to come up with for my company, the WBK logo and the NAQTR logo.
• Lastly, no vertical cards and no split cards (logo on left, contact info on right side).
• Thanks much!

```html
<!DOCTYPE html>
<html lang="en">
<head>
<meta charset="utf-8">
<title>Glimmertide Pool Service – Business Card</title>
<link rel="stylesheet" href="https://fonts.googleapis.com/css2?family=Roboto:wght@300;400;700&display=swap">
<style>
  :root {
    --sky: #e3f1f9;
    --paper: #ffffff;
    --mist: #f4f4f4;
    --mist-back: #eeeeee;
    --brand: #0255a3;
    --brand-light: #3176b5;
    --icon: #1a8fd0;
    --ink: #2a2a2a;
    --pool-deep: #0b4f9a;
    --pool-mid: #1d6fc0;
    --pool-light: #3a8fd6;
    --badge-a: #1f4f9e;
    --badge-b: #e8502e;
  }
  * { box-sizing: border-box; margin: 0; padding: 0; }
  html, body {
    width: 1000px; height: 1200px; overflow: hidden;
    background: var(--paper);
    font-family: "Roboto", Arial, sans-serif;
  }
  .sheet { position: relative; width: 1000px; height: 1200px; }
  .card {
    position: absolute; left: 72px; width: 858px; height: 490px;
    box-shadow: 0 14px 40px rgba(40, 80, 120, 0.18);
    overflow: hidden;
  }
  .card--front { top: 70px; }
  .card--back { top: 641px; }
  .card__art { position: absolute; inset: 0; width: 858px; height: 490px; }

  .brand { position: absolute; left: 58px; top: 48px; color: var(--brand); }
  .brand__web { font-size: 17px; letter-spacing: 1px; color: var(--ink); font-weight: 400; }
  .brand__name {
    margin-top: 4px; font-size: 60px; line-height: 1; font-weight: 700;
    letter-spacing: 1px; color: var(--brand);
  }
  .brand__sub {
    margin-top: 6px; font-size: 28px; font-weight: 700; letter-spacing: 17px;
    color: var(--brand);
  }

  .person { position: absolute; right: 60px; top: 238px; text-align: right; color: var(--paper); }
  .person__name { font-size: 62px; font-weight: 300; line-height: 1; }
  .person__role { margin-top: 2px; margin-right: 30px; font-size: 17px; letter-spacing: 7px; font-weight: 400; }

  .contact { position: absolute; left: 70px; top: 360px; list-style: none; color: var(--ink); font-size: 18px; }
  .contact__item { display: flex; align-items: flex-start; gap: 12px; line-height: 24px; }
  .contact__item + .contact__item { margin-top: 15px; }
  .contact__icon { flex: none; width: 26px; height: 26px; }

  .badges { position: absolute; left: 78px; top: 269px; display: flex; gap: 22px; }
  .badge { width: 122px; height: 122px; }

  .services {
    position: absolute; left: 408px; top: 250px; list-style: none;
    color: var(--ink); font-size: 19px; line-height: 24.3px;
  }
</style>
</head>
<body>
<main class="sheet">

  <section class="card card--front" aria-label="Business card front">
    <svg class="card__art" viewBox="0 0 858 490" aria-hidden="false">
      <defs>
        <linearGradient id="pool-front" x1="0" y1="0" x2="1" y2="1">
          <stop offset="0" stop-color="var(--pool-deep)"/>
          <stop offset="0.55" stop-color="var(--pool-mid)"/>
          <stop offset="1" stop-color="var(--pool-light)"/>
        </linearGradient>
      </defs>
      <rect width="858" height="490" fill="var(--sky)"/>
      <polygon points="0,238 270,298 858,16 858,490 0,490" fill="var(--paper)"/>
      <polygon points="0,260 858,452 858,490 0,490" fill="var(--mist)"/>
      <polygon class="card__pool" points="303,308 858,38 858,432" fill="url(#pool-front)"
               role="img" aria-label="Photo of clear blue pool water with a steel ladder"/>
    </svg>

    <div class="brand">
      <p class="brand__web">www.glimmertidepoolservice.example</p>
      <p class="brand__name">GLIMMERTIDE</p>
      <p class="brand__sub">POOL SERVICE</p>
    </div>

    <div class="person">
      <p class="person__name">Dale Wexby</p>
      <p class="person__role">OWNER</p>
    </div>

    <ul class="contact">
      <li class="contact__item">
        <svg class="contact__icon" viewBox="0 0 26 26" aria-hidden="true">
          <circle cx="13" cy="13" r="13" fill="var(--icon)"/>
          <path d="M13 6a4.5 4.5 0 0 0-4.5 4.5c0 3.4 4.5 8.5 4.5 8.5s4.5-5.1 4.5-8.5A4.5 4.5 0 0 0 13 6z" fill="#fff"/>
          <circle cx="13" cy="10.5" r="1.7" fill="var(--icon)"/>
        </svg>
        <span>4817 Quarry Bend Ave.<br>#512 San Diego, CA</span>
      </li>
      <li class="contact__item">
        <svg class="contact__icon" viewBox="0 0 26 26" aria-hidden="true">
          <circle cx="13" cy="13" r="13" fill="var(--icon)"/>
          <path d="M9.3 6.8l2 2.6c.3.4.3 1-.1 1.4l-1 1c.8 1.6 2.1 2.9 3.7 3.7l1-1c.4-.4 1-.4 1.4-.1l2.6 2c.4.3.5.9.1 1.3l-1.2 1.3c-.6.6-1.5.8-2.3.5-3.5-1.3-6.2-4-7.5-7.5-.3-.8-.1-1.7.5-2.3L8 6.7c.4-.4 1-.3 1.3.1z" fill="#fff"/>
        </svg>
        <span>2417 858-291-6083</span>
      </li>
    </ul>
  </section>

  <section class="card card--back" aria-label="Business card back">
    <svg class="card__art" viewBox="0 0 858 490">
      <defs>
        <linearGradient id="pool-back" x1="0" y1="0" x2="1" y2="1">
          <stop offset="0" stop-color="var(--pool-deep)"/>
          <stop offset="0.6" stop-color="var(--pool-mid)"/>
          <stop offset="1" stop-color="var(--pool-light)"/>
        </linearGradient>
      </defs>
      <rect width="858" height="490" fill="var(--paper)"/>
      <polygon points="0,0 455,0 0,205" fill="var(--sky)"/>
      <polygon points="0,232 280,106 858,244 858,490 0,490" fill="var(--mist-back)"/>
      <polygon class="card__pool" points="308,82 530,0 858,0 858,212" fill="url(#pool-back)"
               role="img" aria-label="Photo of clear blue pool water with a steel ladder"/>
    </svg>

    <div class="badges">
      <svg class="badge" viewBox="0 0 122 122" role="img" aria-label="Pool operator certification badge">
        <circle cx="61" cy="61" r="60" fill="#fff"/>
        <circle cx="61" cy="61" r="52" fill="var(--badge-a)"/>
      </svg>
      <svg class="badge" viewBox="0 0 122 122" role="img" aria-label="Pool service association membership badge">
        <circle cx="61" cy="61" r="60" fill="#fff"/>
        <circle cx="61" cy="61" r="52" fill="var(--badge-b)"/>
      </svg>
    </div>

    <ul class="services">
      <li>- Free Estimates</li>
      <li>- Residential and Commercial Services</li>
      <li>- Equipment Repairs</li>
      <li>- Saltwater Systems</li>
      <li>- Licensed, Bonded, Insured</li>
      <li>- Family Owned and Operated</li>
      <li>- No Contracts</li>
    </ul>
  </section>

</main>
</body>
</html>
```